Selling High quality Eco-windows. brisklodge.co.uk

I need a logo and website to market and sell high quality triple glazed windows and Passive House certified windows. These windows can be supply only or supply and fit. They are very energy efficient with low U Values. They are made of timber not PVC or metal. I already run a small Eco-building outfit, completing roofing jobs and renovations with attention to quality detailing, energy conservation and renewable energy systems. I am inspired by Scandinavian simplicity and modern architecture. I am a keen environmentalist.

Target Market(s)

Environmentally aware home owners. Wealthier holiday home owners. Eco house projects. Energy efficient renovations.

Industry/Entity Type

Construction

Number of Pages Required

1 page

Font styles to use
Sans Serif

Colors
2fb6a2
ede9f3
3277b5

Requirements
Must have
• Great images. Eco feel but not 'rustic'. Bold and modern but not 'Stately plans'.
• Affordable. Message: "They will save you energy in the long run. Why loose heat through poor quality glazing? These windows will pay for themselves over time in lower energy bills"
• Optimized for tablets and smart phones.
Nice to have
• Scandinavian inspired. Real wood and not plastic.
• See documents below for existing images and colours.
Should not have
• Should not look, earthy, hippy or rustic. But also not incredibly flash Stately Plans style. These windows are affordable to the average person but great quality. They will add value to any building.

```html
<!DOCTYPE html>
<html lang="en">
<head>
<meta charset="utf-8">
<title>Brisk Lodge — Eco Windows</title>
<link href="https://fonts.googleapis.com/css2?family=Open+Sans:wght@400;600;700&display=swap" rel="stylesheet">
<style>
:root{
  --green:#1c9a7b;
  --green-dark:#16805f;
  --green-bar:#1a9574;
  --teal:#2fb6a2;
  --ink:#555;
  --ink-dark:#444;
  --line:#dcdcdc;
  --blue:#3277b5;
  --red:#c1575f;
  --amber:#dba72d;
  --grey:#9b9b9b;
  --white:#fff;
}
*{box-sizing:border-box;margin:0;padding:0}
html,body{width:1200px;height:2429px;overflow:hidden}
body{position:relative;background:var(--white);font-family:"Open Sans",Arial,sans-serif;color:var(--ink)}
.abs{position:absolute}

/* top bar */
.topbar{left:0;top:0;width:1200px;height:36px;background:var(--green-bar);color:var(--white);font-size:11.5px}
.topbar .item{position:absolute;top:10px;display:flex;align-items:center;gap:8px}
.topbar svg{width:12px;height:12px;fill:var(--white)}

/* header */
.header{left:0;top:36px;width:1200px;height:74px;background:var(--white);border-bottom:1px solid #eee}
.brand{position:absolute;left:100px;top:22px;display:flex;align-items:center;gap:10px}
.brand-mark{width:30px;height:30px;background:var(--green)}
.brand-name{font-size:21px;font-weight:400;color:#4a4a4a;letter-spacing:.5px}
.nav{position:absolute;left:366px;top:0;display:flex;height:74px}
.nav a{display:block;height:74px;padding:22px 0 0 10px;border-right:1px solid var(--line);text-decoration:none}
.nav .t{display:block;font-size:11.5px;font-weight:700;color:#333}
.nav .s{display:block;font-size:11px;color:#777;margin-top:3px}

/* hero */
.hero{left:0;top:110px;width:1200px;height:491px;background:linear-gradient(180deg,#cfd7d8 0%,#e6e9e6 38%,#b7b6ae 62%,#a29f99 100%)}
.hero-caption{left:100px;top:398px;width:407px;height:136px;background:rgba(35,35,35,.82);border-left:8px solid var(--green);padding:20px 22px}
.hero-caption h1{font-size:27px;font-weight:600;color:var(--teal);letter-spacing:.5px}
.hero-caption p{font-size:19px;color:#f0f0f0;line-height:28px;margin-top:6px;text-transform:uppercase}
.dots{display:flex;gap:6px}
.dots span{width:8px;height:8px;border-radius:50%;background:#fff}
.dots .on{background:var(--green)}
.dots.grey span{background:#ccc}
.dots.grey .on{background:var(--green)}

/* section titles */
.sec-title{left:0;width:1200px;text-align:center;font-size:24px;font-weight:600;color:#555}
.sec-rule{left:575px;width:50px;height:3px;background:var(--green)}
.lead{text-align:center;font-size:11.5px;line-height:26.5px;color:#555}

/* promo cards */
.card{top:855px;width:487px;height:273px;overflow:hidden;box-shadow:0 14px 14px -8px rgba(0,0,0,.25)}
.card .photo{position:absolute;inset:0}
.card .overlay{position:absolute;left:0;bottom:0;width:100%;height:106px}
.card .overlay svg{position:absolute;inset:0;width:100%;height:100%}
.card h3{position:absolute;left:25px;top:20px;font-size:16.5px;font-weight:700;color:#fff;text-transform:uppercase}
.card p{position:absolute;left:25px;top:44px;width:250px;font-size:11.5px;line-height:23px;color:#fff}
.badge{position:absolute}

/* portfolio */
.folio{top:1355px;width:242px;height:235px}
.folio .photo{height:178px}
.folio .label{height:57px;text-align:center;color:#fff;padding-top:12px}
.folio .label b{display:block;font-size:12px;font-weight:700}
.folio .label i{display:block;font-size:10.5px;margin-top:3px}

/* features */
.feature{top:1709px;width:290px;text-align:center}
.feature .icon{width:104px;height:104px;border-radius:50%;margin:0 auto;display:flex;align-items:center;justify-content:center}
.feature h4{font-size:17px;font-weight:600;color:#555;margin-top:34px}
.feature p{font-size:11.5px;line-height:25px;color:#555;margin-top:14px}
.btn{display:inline-block;width:116px;height:35px;line-height:35px;background:var(--green);color:#fff;font-size:11px;margin-top:23px;text-decoration:none}
.divider{top:1773px;width:1px;height:205px;background:var(--line)}

/* footer */
.footer{left:0;top:2097px;width:1200px;height:286px;background:var(--green)}
.footer h5{position:absolute;font-size:14px;font-weight:700;color:#fff}
.post{position:absolute;left:100px;width:270px;color:#fff}
.post b{display:block;font-size:11.5px;font-weight:700}
.post span{display:block;font-size:11.5px;margin-top:6px}
.post-rule{position:absolute;left:100px;width:270px;height:1px;background:rgba(255,255,255,.25)}
.links{position:absolute;list-style:none;color:#fff;font-size:11.5px;line-height:24px}
.social{position:absolute;left:896px;top:2201px;display:flex;gap:7px}
.social span{width:30px;height:30px;border-radius:50%;background:#fff}
.bottombar{left:0;top:2383px;width:1200px;height:46px;background:var(--green-dark);color:#fff;font-size:11.5px;display:flex;justify-content:center;align-items:center;gap:36px}
</style>
</head>
<body>

<!-- top bar -->
<div class="abs topbar">
  <div class="item" style="left:421px">
    <svg viewBox="0 0 12 12"><path d="M6 0a4 4 0 0 0-4 4c0 3 4 8 4 8s4-5 4-8a4 4 0 0 0-4-4zm0 5.5A1.5 1.5 0 1 1 6 2.5a1.5 1.5 0 0 1 0 3z"/></svg>
    120 Street name, State name, Country name : 6523656
  </div>
  <div class="item" style="left:754px">
    <svg viewBox="0 0 12 12"><path d="M2.5 0 4.5 2.5 3.3 4a7 7 0 0 0 4.7 4.7L9.5 7.5 12 9.5 10.5 12C5 12 0 7 0 1.5z"/></svg>
    Call us free : ( 0123 ) 456 789
  </div>
  <div class="item" style="left:958px">
    <svg viewBox="0 0 12 12"><path d="M0 2h12v1L6 7 0 3zM0 4.5l6 4 6-4V10H0z"/></svg>
    info@brisklodge.co.uk
  </div>
</div>

<!-- header -->
<header class="abs header">
  <div class="brand">
    <span class="brand-mark"></span>
    <span class="brand-name">BRISK LODGE</span>
  </div>
  <nav class="nav">
    <a style="width:128px"><span class="t">ABOUT US</span><span class="s">Know our history</span></a>
    <a style="width:150px"><span class="t">OUR PRODUCTS</span><span class="s">Some more products</span></a>
    <a style="width:154px"><span class="t">SERVICES</span><span class="s">View our services</span></a>
    <a style="width:149px"><span class="t">TESTIMONIALS</span><span class="s">Client's feed back</span></a>
    <a style="width:154px"><span class="t">HELP &amp; SUPPORT</span><span class="s">Get in Touch</span></a>
  </nav>
</header>

<!-- hero -->
<section class="abs hero" role="img" aria-label="Bright modern living room with floor-to-ceiling timber windows overlooking a garden and pool"></section>
<div class="abs hero-caption">
  <h1>BRISK LODGE</h1>
  <p>They are very energy efficient and are made of timber.</p>
</div>
<div class="abs dots" style="left:575px;top:574px"><span class="on"></span><span></span><span></span><span></span></div>

<!-- welcome -->
<h2 class="abs sec-title" style="top:659px">WELCOME TO BRISK LODGE</h2>
<div class="abs sec-rule" style="top:704px"></div>
<p class="abs lead" style="left:150px;top:728px;width:900px">Lorem Ipsum is simply dummy text of the printing and typesetting industry. Lorem Ipsum has been the industry's standard dummy text ever since the 1500s, when an unknown printer took a galley of type and scrambled it to make a type specimen book. It has survived not only five centuries, but also the leap into electronic typesetting, remaining essentially unchanged.</p>

<!-- promo cards -->
<article class="abs card" style="left:100px">
  <div class="photo" role="img" aria-label="Modern room with large triple glazed windows and an armchair" style="background:linear-gradient(160deg,#e9ecec 0%,#b9c6b0 40%,#9a9c92 70%,#c9c2b6 100%)"></div>
  <span class="badge" style="left:343px;top:20px;width:102px;height:102px;border-radius:50%;background:#f2a91e"></span>
  <div class="overlay">
    <svg viewBox="0 0 487 106" preserveAspectRatio="none"><polygon points="0,0 250,0 305,106 0,106" fill="#1c9a7b" opacity=".92"/></svg>
    <h3>Triple Glazed Windows</h3>
    <p>Lorem Ipsum is simply dummy text of the printing and typesetting industry... &#9656;</p>
  </div>
</article>
<article class="abs card" style="left:614px">
  <div class="photo" role="img" aria-label="Living room with sofa and tall passive house certified windows" style="background:linear-gradient(160deg,#d9d4c8 0%,#f1eee6 40%,#b9ad98 75%,#8f8577 100%)"></div>
  <span class="badge" style="left:300px;top:20px;width:60px;height:60px;background:#d9342b"></span>
  <div class="overlay">
    <svg viewBox="0 0 487 106" preserveAspectRatio="none"><polygon points="0,0 250,0 305,106 0,106" fill="#1c9a7b" opacity=".92"/></svg>
    <h3>Triple Glazed Windows</h3>
    <p>Lorem Ipsum is simply dummy text of the printing and typesetting industry... &#9656;</p>
  </div>
</article>

<!-- portfolio -->
<h2 class="abs sec-title" style="top:1193px">PORTFOLIO</h2>
<p class="abs lead" style="left:205px;top:1264px;width:790px">Lorem Ipsum is simply dummy text of the printing and typesetting industry. Lorem Ipsum has been the industry's standard dummy text ever since the 1500s, when an unknown printer took a galley of type and scrambled it to make a type specimen book.</p>

<div class="abs folio" style="left:100px">
  <div class="photo" role="img" aria-label="Cross-section of a dark timber window frame" style="background:linear-gradient(135deg,#2d2d2d,#6d6a66 55%,#b08357)"></div>
  <div class="label" style="background:var(--blue)"><b>LOREM IPSUM IS SIMPLY</b><i>Click here for view details</i></div>
</div>
<div class="abs folio" style="left:353px">
  <div class="photo" role="img" aria-label="Cross-section of a pine timber window frame with glazing" style="background:linear-gradient(135deg,#f4f4f4,#d29a4a 50%,#b8782e)"></div>
  <div class="label" style="background:var(--red)"><b>LOREM IPSUM IS SIMPLY</b><i>Click here for view details</i></div>
</div>
<div class="abs folio" style="left:605px">
  <div class="photo" role="img" aria-label="Cross-section of a white window profile with triple glazing" style="background:linear-gradient(135deg,#fafafa,#d8dcdc 55%,#9aa)"></div>
  <div class="label" style="background:var(--amber)"><b>LOREM IPSUM IS SIMPLY</b><i>Click here for view details</i></div>
</div>
<div class="abs folio" style="left:858px">
  <div class="photo" role="img" aria-label="Cross-section of a white window frame with dark glazing" style="background:linear-gradient(135deg,#dcdcdc,#f2f2f2 50%,#555)"></div>
  <div class="label" style="background:var(--grey)"><b>LOREM IPSUM IS SIMPLY</b><i>Click here for view details</i></div>
</div>
<div class="abs dots grey" style="left:584px;top:1630px"><span class="on"></span><span></span><span></span></div>

<!-- features -->
<div class="abs feature" style="left:90px">
  <div class="icon" style="background:var(--red)">
    <svg width="46" height="46" viewBox="0 0 46 46" fill="none" stroke="#fff" stroke-width="3" stroke-linecap="round"><path d="M34 6C22 10 14 20 12 34"/><path d="M34 6c-2 10-8 18-18 22"/><path d="M8 40c4-2 8 2 12 0s6 2 10 0"/></svg>
  </div>
  <h4>OUR STORY</h4>
  <p>Lorem Ipsum is simply dummy<br>text of the printing and typesetting industry. Lorem Ipsum has been the industry's standard dummy text ever since the 1500s...</p>
  <a class="btn">READ MORE</a>
</div>
<div class="abs divider" style="left:413px"></div>
<div class="abs feature" style="left:446px">
  <div class="icon" style="background:var(--amber)">
    <svg width="50" height="44" viewBox="0 0 50 44" fill="#fff"><path d="M2 4h28v18H14l-7 6v-6H2z"/><path d="M34 12h14v18h-5v6l-7-6H20v-5h14z"/><rect x="8" y="11" width="3" height="3" fill="#dba72d"/><rect x="14" y="11" width="3" height="3" fill="#dba72d"/><rect x="20" y="11" width="3" height="3" fill="#dba72d"/></svg>
  </div>
  <h4>FEED BACKS</h4>
  <p>Lorem Ipsum is simply dummy<br>text of the printing and typesetting industry. Lorem Ipsum has been the industry's standard dummy text ever since the 1500s...</p>
  <a class="btn">READ MORE</a>
</div>
<div class="abs divider" style="left:782px"></div>
<div class="abs feature" style="left:817px">
  <div class="icon" style="background:#34b3e4">
    <svg width="46" height="46" viewBox="0 0 46 46" fill="none" stroke="#fff" stroke-width="3.5" stroke-linejoin="round"><path d="M24 8H8v30h30V22"/><path d="M36 5l5 5-17 17-7 2 2-7z" fill="#fff"/></svg>
  </div>
  <h4>FEATURES</h4>
  <p>Lorem Ipsum is simply dummy<br>text of the printing and typesetting industry. Lorem Ipsum has been the industry's standard dummy text ever since the 1500s...</p>
  <a class="btn">READ MORE</a>
</div>

<!-- footer -->
<footer class="abs footer"></footer>
<h5 class="abs" style="left:100px;top:2134px;font-size:14px;font-weight:700;color:#fff">LATEST POSTS</h5>
<span class="abs" style="left:352px;top:2132px;color:#fff;font-size:13px">&lsaquo; &rsaquo;</span>
<div class="post" style="top:2170px"><b>Lorem Ipsum is simply dummy text of the printing</b><span>Posted on 27 March 2015</span></div>
<div class="post-rule" style="top:2226px"></div>
<div class="post" style="top:2236px"><b>Lorem Ipsum is simply dummy text of the printing</b><span>Posted on 27 March 2015</span></div>
<div class="post-rule" style="top:2292px"></div>
<div class="post" style="top:2303px"><b>Lorem Ipsum is simply dummy text of the printing</b><span>Posted on 27 March 2015</span></div>

<h5 class="abs" style="left:445px;top:2134px;font-size:14px;font-weight:700;color:#fff">PRODUCTS</h5>
<ul class="links" style="left:446px;top:2164px">
  <li>Lorem Ipsum is simply dummy</li><li>Lorem Ipsum</li><li>Lorem Ipsum is simply</li><li>Lorem Ipsum is simply dummy</li><li>Lorem Ipsum is sim</li><li>Lorem Ipsum is simply dummy</li><li>Lorem Ipsum</li>
</ul>
<ul class="links" style="left:669px;top:2164px">
  <li>Lorem Ipsum is</li><li>Lorem Ipsum</li><li>Lorem Ipsum is simply</li><li>Lorem Ipsum is simply dummy</li><li>Lorem Ipsum is sim</li><li>Lorem Ipsum is simply dummy</li><li>Lorem Ipsum</li>
</ul>

<h5 class="abs" style="left:897px;top:2138px;font-size:14px;font-weight:700;color:#fff">FOLLOW US</h5>
<p class="abs" style="left:897px;top:2167px;font-size:11.5px;color:#fff">Connect with our social media network</p>
<div class="social"><span></span><span></span><span></span><span></span><span></span></div>

<div class="abs bottombar">
  <span>© 2016. Brisk Lodge. All rights reserved.</span>
  <span>Terms of Use</span>
  <span>Privacy Policy</span>
  <span>Site Map</span>
</div>

</body>
</html>
```